Wordpress Lifestyle Blog

Just to be clear - I have the domain and the wordpress site (which is messy). I need someone to help me complete a simple blog design and then go into the existing wordpress site, and get rid of all the existing rubbish and set up the templates please. If we progress with design can we please be clear about additional costs upfront which, of course, I appreciate is the case.

Need a lifestyle blog. It is called brightyearsahead.com. Aimed at the older woman but needs to look fresh and young, not old fashioned. Navigation will be Home, Fashion, Feelings, Fitness, Contact. I have a logo but not sure it will work at the moment so happy with stylised words.Will have social media links.

Need homepage (not overly long) to have a main slider for pics/videos. Then the three category boxes underneath linking through to 2nd level pages containing blogs for that category and then the actual blog page. Happy to be led by expertise if this is not gonna work.

Am really looking for something clean and fresh like a Marwyn type approach to be honest.

If you need any further direction please just ask - once design chosen I am looking to move quickly.

Thank you so much for looking at this brief

Target Market(s)

Women, 40 - 60 age group but with a younger outlook

Number of Pages Required

3 page

Colors

Designer to choose colors to be used in the design.

Requirements
Must have
• Reflect youth, fun, bright
• Lift easily into a wordpress format
Should not have
• Old, staid, frumpy,dark

```html
<!DOCTYPE html>
<html lang="en">
<head>
<meta charset="utf-8">
<title>Bright Years Ahead – 5 Style Lessons From a Closet Clear Out</title>
<link rel="stylesheet" href="https://fonts.googleapis.com/css2?family=Libre+Caslon+Text&family=Montserrat:wght@400;500&display=swap">
<style>
:root{
  --page-bg:#f2efea;
  --white:#ffffff;
  --header-bg:#f8f8f7;
  --ink:#3d3d3d;
  --ink-soft:#555555;
  --accent:#e3c4a2;
  --field:#f4f4f4;
  --line:#d7d7d7;
}
*{margin:0;padding:0;box-sizing:border-box}
html,body{width:712px;height:1200px;overflow:hidden}
body{background:var(--page-bg);font-family:"Montserrat",sans-serif;color:var(--ink);position:relative}
h1,h2{font-weight:400}
.site-header{position:absolute;left:0;top:0;width:712px;height:56px;background:var(--header-bg)}
.brand{position:absolute;left:66px;top:18px;font-family:"Libre Caslon Text",serif;font-size:15px;color:var(--ink);letter-spacing:.3px;white-space:nowrap}
.main-nav{position:absolute;left:0;top:21px;width:540px;height:14px;font-size:10px;letter-spacing:0;white-space:nowrap}
.main-nav span{position:absolute;top:0}
.nav-home{left:240px}
.nav-fashion{left:289px}
.nav-feelings{left:351px}
.nav-fitness{left:417px}
.nav-contact{left:476px}
.social{position:absolute;display:flex;align-items:center}
.social span{display:block;width:8px;height:8px;border-radius:50%;background:var(--ink)}
.header-social{left:546px;top:24px;gap:17px}
.search{position:absolute;left:644px;top:23px}
.post-card{position:absolute;left:58px;top:107px;width:595px;height:823px;background:var(--white)}
.post-title{position:absolute;left:0;top:24px;width:100%;text-align:center;font-family:"Libre Caslon Text",serif;font-size:18px;color:var(--ink)}
.post-meta{position:absolute;left:0;top:64px;width:100%;text-align:center;font-size:9px;letter-spacing:.3px;color:var(--ink-soft)}
.post-meta .sep{margin:0 10px}
.hero{position:absolute;left:63px;top:105px;width:469px;height:260px;background:linear-gradient(90deg,#cfcccc 0%,#b9b8c6 35%,#cdb9d6 60%,#c9c3cc 100%)}
.post-body{position:absolute;left:60px;top:385px;width:475px;text-align:center;font-size:8.2px;letter-spacing:-.1px;line-height:19.7px;color:var(--ink-soft);white-space:nowrap}
.share{position:absolute;left:0;top:563px;width:100%;display:flex;justify-content:center;align-items:center;gap:10px;font-size:9.5px;color:var(--ink)}
.share .dots{display:flex;gap:9px;margin-left:6px}
.share .dots span{width:7px;height:7px;border-radius:50%;background:var(--accent)}
.related-title{position:absolute;left:0;top:596px;width:100%;text-align:center;font-family:"Libre Caslon Text",serif;font-size:12.5px;letter-spacing:.3px;color:var(--ink)}
.related{position:absolute;left:60px;top:629px;display:flex;gap:15px}
.related-item{width:149px;text-align:center}
.related-item .thumb{width:149px;height:119px}
.related-item .caption{margin-top:10px;font-family:"Libre Caslon Text",serif;font-size:11.5px;line-height:23px;color:var(--ink)}
.thumb.white-dresses{background:linear-gradient(180deg,#8a9b6e 0%,#e8e6e1 55%,#cfc8bb 100%)}
.thumb.pink-flowers{background:linear-gradient(135deg,#d6337e 0%,#e1699f 45%,#c8cbe0 100%)}
.thumb.street-pair{background:linear-gradient(90deg,#8d8f8c 0%,#8a9ab3 45%,#d8473a 75%,#b9bcbf 100%)}
.pager{position:absolute;top:943px;font-size:11px;color:var(--ink)}
.pager.prev{left:59px}
.pager.next{right:59px}
.comments-title{position:absolute;left:0;top:960px;width:712px;text-align:center;font-family:"Libre Caslon Text",serif;font-size:12.5px;color:var(--ink)}
.comment-field{position:absolute;left:214px;top:994px;width:284px;height:53px;background:var(--field);border:1px solid var(--line)}
.post-button{position:absolute;left:295px;top:1066px;width:123px;height:24px;background:var(--accent);color:var(--white);font-size:11px;line-height:24px;text-align:center;letter-spacing:.3px}
.site-footer{position:absolute;left:0;top:1123px;width:712px;height:77px;background:var(--white);border-top:1px solid #e6e3de}
.footer-social{left:315px;top:26px;gap:18px}
.copyright{position:absolute;left:0;top:55px;width:100%;text-align:center;font-size:8.5px;font-weight:500;color:var(--ink)}
</style>
</head>
<body>
<header class="site-header">
  <div class="brand">Bright Years Ahead</div>
  <nav class="main-nav"><span class="nav-home">HOME</span><span class="nav-fashion">FASHION</span><span class="nav-feelings">FEELINGS</span><span class="nav-fitness">FITNESS</span><span class="nav-contact">CONTACT</span></nav>
  <div class="social header-social" aria-label="Social links"><span></span><span></span><span></span><span></span></div>
  <svg class="search" width="9" height="9" viewBox="0 0 10 10" aria-label="Search"><circle cx="4.2" cy="4.2" r="3.3" fill="none" stroke="#3d3d3d" stroke-width="1.3"/><line x1="6.6" y1="6.6" x2="9.3" y2="9.3" stroke="#3d3d3d" stroke-width="1.3"/></svg>
</header>

<article class="post-card">
  <h1 class="post-title">5 Style Lessons From a Closet Clear Out</h1>
  <div class="post-meta">FASHION<span class="sep">|</span>9TH MAI 2018</div>
  <div class="hero" role="img" aria-label="Four smiling women in pastel loungewear posing together"></div>
  <p class="post-body">Lorem ipsum dolor sit amet, consectetur adipiscing elit. Ut tincidunt tortor eget felis vulputate<br>sagittis. Sed eget turpis tincidunt, vestibulum turpis non, tincidunt purus. Vivamus tristique leo eu<br>est tristique interdum. Nam sit amet ligula magna. Pellentesque habitant morbi tristique senectus<br>et netus et malesuada fames ac turpis egestas. Nullam nec congue odio, vitae convallis massa.<br>Nam augue dui, ullamcorper nec sem et, tempus ultricies sem. Phasellus enim felis, iaculis in<br>porta sit amet, sagittis et tellus. Sed molestie purus tellus, interdum bibendum turpis convallis at.<br>Nulla placerat neque viverra, volutpat lacus vel, sodales justo. Vestibulum nec purus eu dolor<br>hendrerit mollis. Aenean non nulla lectus. In laoreet ultricies sodales. Duis nec ex nec sapien</p>
  <div class="share">SHARE THE POST :<div class="dots"><span></span><span></span><span></span></div></div>
  <h2 class="related-title">YOU MIGHT ALSO LIKE</h2>
  <div class="related">
    <div class="related-item"><div class="thumb white-dresses" role="img" aria-label="Four women in white summer dresses and hats outdoors"></div><div class="caption">Aenean non nulla<br>lectus aenean</div></div>
    <div class="related-item"><div class="thumb pink-flowers" role="img" aria-label="Woman in a white jacket in front of pink flowers"></div><div class="caption">Aenean non nulla<br>lectus aenean</div></div>
    <div class="related-item"><div class="thumb street-pair" role="img" aria-label="Two women in a checked suit and red floral dress on a street"></div><div class="caption">Aenean non nulla<br>lectus aenean</div></div>
  </div>
</article>

<div class="pager prev">« PREVIOUS</div>
<div class="pager next">NEXT »</div>
<h2 class="comments-title">COMMENTS</h2>
<div class="comment-field"></div>
<div class="post-button">POST</div>

<footer class="site-footer">
  <div class="social footer-social" aria-label="Social links"><span></span><span></span><span></span><span></span></div>
  <div class="copyright">© 2018 COPYRIGHT BRIGHT YEARS AHEAD</div>
</footer>
</body>
</html>
```